Digital Marketing Website Design

I need the homepage designed for my new digital marketing agency I am starting. The main goal for this homepage is to drive people to make an appointment for me to discuss their upcoming projects. Here are some examples of the layouts that I would like to emulate.
https://www.tallmarsh.com/
https://www.quillforge.com/
https://pebblenook.com/
https://drvenholt.com/
https://www.quietlyrooted.org/
My main focus is to attract leads that need help with running digital ads such as Chatterly ads and Finder Promos. I do offer other services like SEO and other things but the main focus is digital Ads.
The final design should communicate Orchid Digital is a Digital marketing strategist building predictable revenue for small businesses through digital ads, email and marketing automation.
Target Market(s)
30-55, business owners, income 100K+, ecommerce companies, etc.
Industry/Entity Type
Digital Marketing
Number of Pages Required
2 page
Font styles to use
Requirements
Must have
- An appealing look and feel set to drive people to make an appointment.
Logo
There needs to be a call to action button in the far right of the navigation
The same call to action in the navigation needs to be in each section on the homepage.
I need the homepage and an about us page.

```html
<!DOCTYPE html>
<html lang="en">
<head>
<meta charset="utf-8">
<title>Orchid Digital — Predictable Revenue for Small Businesses</title>
<link href="https://fonts.googleapis.com/css2?family=Hind:wght@500;600;700&family=Montserrat:wght@600;700&family=Open+Sans:wght@400&family=Arimo:wght@400;700&display=swap" rel="stylesheet">
<style>
:root{
  --orange:#f47a20;
  --orange-red:#ec4a2c;
  --ink:#2b2b2b;
  --muted:#8a8a8a;
  --soft-bg:#f8f8f8;
  --white:#ffffff;
  --black:#000000;
  --logo-grey:#9a9a9a;
}
*{margin:0;padding:0;box-sizing:border-box}
html,body{width:1200px;height:2405px;overflow:hidden;background:var(--white)}
body{position:relative;font-family:"Arimo",Arial,sans-serif;color:var(--ink)}
.abs{position:absolute}
.site-header{position:absolute;left:0;top:0;width:1200px;height:95px;background:var(--white)}
.brand{position:absolute;font-family:"Montserrat",sans-serif;font-weight:700;font-size:27px;letter-spacing:-0.5px;color:var(--orange-red);display:flex;align-items:center;gap:7px}
.brand .dot{width:12px;height:12px;background:var(--orange);border-radius:50%}
.site-header .brand{left:54px;top:31px}
.main-nav a{position:absolute;top:38px;font-family:"Montserrat",sans-serif;font-weight:600;font-size:14.5px;color:var(--muted);text-decoration:none;letter-spacing:0.2px}
.main-nav a.active{color:var(--ink)}
.btn{display:flex;align-items:center;justify-content:center;font-family:"Arimo",sans-serif;font-weight:700;text-decoration:none;text-transform:uppercase;border-radius:30px}
.btn-nav{position:absolute;left:888px;top:23px;width:244px;height:48px;background:linear-gradient(90deg,var(--orange),var(--orange-red));color:var(--white);font-family:"Montserrat",sans-serif;font-size:14.5px}
.hero{position:absolute;left:0;top:95px;width:1200px;height:660px;background:linear-gradient(120deg,#8a7a6a 0%,#6d5d4e 30%,#a3886c 55%,#5a4a3e 80%,#2c3440 100%)}
.hero-shade{position:absolute;inset:0;background:rgba(0,0,0,0.28)}
.hero h1{position:absolute;left:0;width:1200px;top:191px;text-align:center;font-family:"Hind",sans-serif;font-weight:700;font-size:46px;line-height:49px;color:var(--white);text-shadow:0 2px 6px rgba(0,0,0,.35)}
.hero p{position:absolute;left:0;width:1200px;top:298px;text-align:center;font-size:23px;line-height:32px;color:var(--white)}
.btn-hero{position:absolute;top:389px;width:315px;height:57px;font-size:15px;color:var(--white)}
.btn-hero.solid{left:283px;background:linear-gradient(90deg,var(--orange),var(--orange-red))}
.btn-hero.ghost{left:610px;border:2px solid var(--white)}
.chev{position:absolute}
.partners{position:absolute;left:0;top:755px;width:1200px;height:110px;border-bottom:1px solid #e2e2e2;background:var(--white)}
.partners span{position:absolute;top:40px;transform:translateX(-50%);font-family:"Hind",sans-serif;font-weight:600;font-size:26px;color:var(--logo-grey)}
.how{position:absolute;left:0;top:865px;width:1200px;height:735px;background:var(--soft-bg)}
.how h2{position:absolute;left:0;width:1200px;top:75px;text-align:center;font-family:"Hind",sans-serif;font-weight:600;font-size:33px;color:#333}
.how .intro{position:absolute;left:155px;width:890px;top:127px;text-align:center;font-family:"Open Sans",sans-serif;font-size:16px;line-height:31px;color:#333}
.how h3{position:absolute;left:0;width:1200px;top:354px;text-align:center;font-family:"Hind",sans-serif;font-weight:600;font-size:20px;color:#222}
.step-hex{position:absolute;top:406px}
.step-line{position:absolute;top:464px;height:0;border-top:2px dotted #b8b8b8}
.step-text{position:absolute;top:537px;width:270px;text-align:center;font-size:19px;line-height:27px;color:#222}
.testimonials{position:absolute;left:0;top:1600px;width:1200px;height:498px;background:linear-gradient(90deg,var(--orange) 0%,#ee5c2a 60%,var(--orange-red) 100%)}
.testimonials h2{position:absolute;left:0;width:1200px;top:58px;text-align:center;font-family:"Hind",sans-serif;font-weight:600;font-size:36px;color:var(--white);letter-spacing:0.5px}
.card{position:absolute;top:185px;width:299px;height:213px;border:1px solid rgba(255,255,255,.9)}
.avatar{position:absolute;left:104px;top:-45px;width:90px;height:90px;border-radius:50%;background:linear-gradient(160deg,#c9c4bd,#5f5a57);border:2px solid var(--white)}
.card blockquote{position:absolute;left:20px;right:20px;top:66px;text-align:center;font-size:14.5px;line-height:23.5px;color:var(--white)}
.card cite{position:absolute;left:0;right:0;top:168px;text-align:center;font-style:normal;font-weight:700;font-size:14.5px;color:var(--white)}
.site-footer{position:absolute;left:0;top:2098px;width:1200px;height:307px;background:var(--black);color:var(--white)}
.site-footer .brand{left:130px;top:70px}
.legal{position:absolute;left:134px;top:140px;font-size:14px;line-height:24px;color:#d8d8d8}
.legal .links{font-size:15px}
.foot-col{position:absolute;top:72px}
.foot-col h4{font-family:"Hind",sans-serif;font-weight:600;font-size:21px;letter-spacing:0.3px;margin-bottom:8px}
.foot-col li{list-style:none;font-size:14px;line-height:24.7px;padding-left:4px}
.contact li{position:relative;padding-left:26px}
.contact svg{position:absolute;left:0;top:5px}
</style>
</head>
<body>

<header class="site-header">
  <div class="brand"><span class="dot"></span>ORCHID DIGITAL</div>
  <nav class="main-nav">
    <a class="active" style="left:420px">ABOUT</a>
    <a style="left:512px">HOW IT WORKS</a>
    <a style="left:677px">WHAT PEOPLE SAYS</a>
  </nav>
  <a class="btn btn-nav">Schedule Appointment</a>
</header>

<section class="hero">
  <div role="img" aria-label="Photo of a team working together at desks in a bright office" style="position:absolute;inset:0"></div>
  <div class="hero-shade"></div>
  <h1>We Built Profitable Ad Campaigns<br>For small businesses</h1>
  <p>The selling system that brings in Predictable revenue through<br>digital ads, email, and marketing automation.</p>
  <a class="btn btn-hero solid">Free Chatterly Ads Checklist</a>
  <a class="btn btn-hero ghost">Schedule an Appointment</a>
  <svg class="chev" style="left:64px;top:286px" width="26" height="40" viewBox="0 0 26 40"><path d="M22 3 L5 20 L22 37" fill="none" stroke="#fff" stroke-width="5"/></svg>
  <svg class="chev" style="left:1128px;top:284px" width="26" height="40" viewBox="0 0 26 40"><path d="M4 3 L21 20 L4 37" fill="none" stroke="#fff" stroke-width="5"/></svg>
</section>

<section class="partners">
  <span style="left:215px">Kestrel</span>
  <span style="left:370px">Ouvana</span>
  <span style="left:530px">Tandemry</span>
  <span style="left:686px">Velmora</span>
  <span style="left:848px">Mossway</span>
  <span style="left:1002px">Brightfold</span>
</section>

<section class="how">
  <svg class="abs" style="left:585px;top:32px" width="24" height="32" viewBox="0 0 24 32"><path d="M12 2 C15 8 22 12 20 22 C19 28 15 31 12 31 C7 31 3 27 4 21 C5 16 8 15 9 11 C11 14 11 16 12 17 C14 12 13 7 12 2Z" fill="var(--orange-red)"/></svg>
  <h2>How it Works</h2>
  <p class="intro">At Orchid Digital we know that you want to have a profitable business. In order to do that, you need a strong system that can predictably bring in sales even in bad times. The problem is there is so much out there to wade through and so many people telling you what you should do which makes you feel frustrated, lost, and flat out stressed out. We believe that businesses with great products should get the customer.<br>We understand the frustration which is why we are here to help you maneuver through the minutiae and create a system that flat out works.</p>
  <h3>Here’s how we do it:</h3>

  <svg class="step-hex" style="left:210px" width="104" height="116" viewBox="0 0 104 116"><path d="M52 2 L100 30 L100 86 L52 114 L4 86 L4 30Z" fill="#fff" stroke="#eee" stroke-width="2"/><rect x="26" y="34" width="52" height="46" rx="5" fill="none" stroke="var(--orange-red)" stroke-width="3"/><line x1="26" y1="46" x2="78" y2="46" stroke="var(--orange-red)" stroke-width="3"/><path d="M32 66 L36 70 L43 62" fill="none" stroke="var(--orange-red)" stroke-width="3"/><circle cx="52" cy="58" r="3" fill="none" stroke="var(--orange-red)" stroke-width="2"/><circle cx="62" cy="58" r="3" fill="none" stroke="var(--orange-red)" stroke-width="2"/><circle cx="70" cy="68" r="3" fill="none" stroke="var(--orange-red)" stroke-width="2"/></svg>
  <div class="step-line" style="left:323px;width:215px"></div>
  <svg class="step-hex" style="left:550px" width="104" height="116" viewBox="0 0 104 116"><defs><linearGradient id="hexg" x1="0" y1="0" x2="0" y2="1"><stop offset="0" stop-color="#f4781f"/><stop offset="1" stop-color="#ec4a2c"/></linearGradient></defs><path d="M52 2 L100 30 L100 86 L52 114 L4 86 L4 30Z" fill="url(#hexg)"/><circle cx="38" cy="50" r="7" fill="none" stroke="#fff" stroke-width="3"/><circle cx="66" cy="50" r="7" fill="none" stroke="#fff" stroke-width="3"/><circle cx="52" cy="44" r="8" fill="none" stroke="#fff" stroke-width="3"/><path d="M30 82 V70 Q38 60 46 70 M58 70 Q66 60 74 70 V82 M40 82 V66 Q52 54 64 66 V82" fill="none" stroke="#fff" stroke-width="3"/></svg>
  <div class="step-line" style="left:662px;width:215px"></div>
  <svg class="step-hex" style="left:885px" width="104" height="116" viewBox="0 0 104 116"><path d="M52 2 L100 30 L100 86 L52 114 L4 86 L4 30Z" fill="#fff" stroke="#eee" stroke-width="2"/><path d="M40 84 V74 Q30 70 34 60 Q34 44 52 42 Q68 42 70 58 V84" fill="none" stroke="var(--orange-red)" stroke-width="3"/><circle cx="56" cy="60" r="6" fill="none" stroke="var(--orange-red)" stroke-width="3"/><rect x="30" y="30" width="44" height="6" rx="2" fill="none" stroke="var(--orange-red)" stroke-width="2"/></svg>

  <p class="step-text" style="left:132px">Schedule an appointment to go through the basics of what you need and to find out if we are a good fit to work together.</p>
  <p class="step-text" style="left:470px">Work with our team to build out your customer journey and selling system</p>
  <p class="step-text" style="left:810px;line-height:29px">Execute and enjoy the<br>extra revenue!</p>
</section>

<section class="testimonials">
  <h2>What others are saying</h2>
  <svg class="chev" style="left:76px;top:250px" width="24" height="38" viewBox="0 0 24 38"><path d="M20 3 L5 19 L20 35" fill="none" stroke="#fff" stroke-width="4"/></svg>
  <svg class="chev" style="left:1108px;top:250px" width="24" height="38" viewBox="0 0 24 38"><path d="M4 3 L19 19 L4 35" fill="none" stroke="#fff" stroke-width="4"/></svg>
  <article class="card" style="left:127px"><div class="avatar" role="img" aria-label="Client portrait"></div><blockquote>“Augiat in pede Fusce tellus Sed metus augue convallis et vehicula ut pulvinar eu ante Integer orci tellus tristique vitae consequat nec mauris”</blockquote><cite>By Author Name</cite></article>
  <article class="card" style="left:445px"><div class="avatar" role="img" aria-label="Client portrait"></div><blockquote>“Augiat in pede Fusce tellus Sed metus augue convallis et vehicula ut pulvinar eu ante Integer orci tellus tristique vitae consequat nec mauris”</blockquote><cite>By Author Name</cite></article>
  <article class="card" style="left:763px"><div class="avatar" role="img" aria-label="Client portrait"></div><blockquote>“Augiat in pede Fusce tellus Sed metus augue convallis et vehicula ut pulvinar eu ante Integer orci tellus tristique vitae consequat nec mauris”</blockquote><cite>By Author Name</cite></article>
</section>

<footer class="site-footer">
  <div class="brand"><span class="dot"></span>ORCHID DIGITAL</div>
  <div class="legal">© 2020 Company Name I All Rights Reserved<br><span class="links">Term of use &nbsp;I&nbsp; Privacy Policy</span></div>
  <div class="foot-col" style="left:487px"><h4>COMPANY</h4><ul><li>About Us</li><li>Our Services</li><li>How it Works</li><li>Testimonials</li><li>Contact Us</li></ul></div>
  <div class="foot-col" style="left:678px"><h4>RESOURCES</h4><ul><li>Support</li><li>Flagship</li><li>Case Studies</li><li>Social properties</li></ul></div>
  <div class="foot-col contact" style="left:868px"><h4>CONTACT INFO</h4><ul>
    <li><svg width="14" height="18" viewBox="0 0 14 18"><path d="M7 1 C3 1 1 4 1 7 C1 11 7 17 7 17 C7 17 13 11 13 7 C13 4 11 1 7 1Z" fill="var(--orange)"/><circle cx="7" cy="7" r="2.5" fill="#000"/></svg>48 Harlow Lane Suite 3<br>Austin 78701 TX</li>
    <li><svg width="16" height="16" viewBox="0 0 16 16"><path d="M3 1 L6 4 L4 6 Q6 10 10 12 L12 10 L15 13 L13 15 Q4 14 1 3Z" fill="none" stroke="var(--orange)" stroke-width="1.6"/></svg>(555) 014 2288</li>
    <li><svg width="16" height="12" viewBox="0 0 16 12"><rect x="0" y="0" width="16" height="12" fill="var(--orange)"/><path d="M0 0 L8 7 L16 0" fill="none" stroke="#000" stroke-width="1.4"/></svg>hello@orchiddigital.com</li>
  </ul></div>
</footer>

</body>
</html>
```